https://copperwillowbrambleyard.org/

We would like the website to represent 19th century African American civil war soldier's letters. We would like the site colors to be nice and clean . Along with the layout, including a great landing page , blogs and introduction.

```html
<!DOCTYPE html>
<html lang="en">
<head>
<meta charset="utf-8">
<title>Copperwillow Brambleyard</title>
<link href="https://fonts.googleapis.com/css2?family=Lora:ital,wght@0,400;0,700;1,700&family=Poppins:ital,wght@0,300;0,400;0,600;1,600&display=swap" rel="stylesheet">
<style>
:root{
  --ink:#000;
  --red:#9e0a06;
  --gold:#e5a800;
  --white:#ffffff;
  --field:#f5f5f5;
  --field-text:#b5b5b5;
}
*{margin:0;padding:0;box-sizing:border-box}
html,body{width:1200px;height:4417px;overflow:hidden;background:var(--ink)}
.page{position:relative;width:1200px;height:4417px;overflow:hidden;background:var(--ink);font-family:"Poppins",sans-serif;color:var(--white)}
.abs{position:absolute}
.hero-photo{left:0;top:0;width:1200px;height:830px;background:
  radial-gradient(ellipse 420px 300px at 62% 30%,#8f8f8b 0%,rgba(90,90,87,.6) 45%,rgba(0,0,0,0) 100%),
  linear-gradient(to bottom,#2a2a29 0%,#3a3a38 30%,#1a1a19 70%,#000 100%)}
.field-photo{left:0;top:1380px;width:1200px;height:860px;background:
  radial-gradient(ellipse 380px 420px at 48% 42%,#3c3c3a 0%,#222 55%,rgba(0,0,0,0) 100%),
  linear-gradient(to bottom,#000 0%,#141414 20%,#141414 80%,#000 100%)}
.march-photo{left:0;top:2550px;width:1200px;height:900px;background:
  radial-gradient(ellipse 600px 450px at 50% 50%,#1e201c 0%,#111210 60%,#000 100%)}
.brand{left:65px;top:20px;display:flex;align-items:center;gap:10px;font-family:"Lora",serif;font-weight:700;font-size:18px;letter-spacing:.5px;color:var(--white)}
.brand-dot{width:12px;height:12px;background:var(--red)}
.nav{top:28px;font-family:"Lora",serif;font-size:11px;letter-spacing:2.5px;color:var(--white)}
.search{left:934px;top:22px;width:197px;height:31px;border-bottom:1px solid #bbb;font-size:10px;color:var(--white);padding-left:8px}
.search svg{position:absolute;right:10px;top:2px}
.quote{left:238px;top:620px;width:720px;font-family:"Lora",serif;font-style:italic;font-weight:700;font-size:51px;line-height:54px;color:var(--white)}
.attribution{left:500px;top:776px;width:402px;text-align:right;font-family:"Lora",serif;font-weight:700;font-size:13px;color:var(--white)}
.display{font-family:"Lora",serif;font-weight:700;color:var(--red);line-height:1;white-space:nowrap}
.about-title{left:-12px;top:844px;font-size:350px;letter-spacing:-4px}
.blogs-title{left:328px;top:1607px;font-size:350px;letter-spacing:-4px}
.testimonials-title{left:60px;top:2716px;font-size:188px;letter-spacing:-3px}
.contact-title{left:-14px;top:3400px;font-size:308px;letter-spacing:-6px}
.body-copy{font-size:12.5px;line-height:20px;font-weight:300;color:var(--white)}
.about-copy{left:238px;top:1212px;width:800px}
.about-copy p+p{margin-top:20px}
.intro-right{left:249px;width:792px;text-align:right}
.explore{display:flex;align-items:center;gap:12px;font-family:"Lora",serif;font-weight:700;font-size:13px;color:var(--gold)}
.card{top:2184px;width:296px}
.card-photo{width:296px;height:171px;background:linear-gradient(160deg,#a9a79f,#6b6a64 55%,#3b3b38)}
.card-title{margin-top:20px;font-family:"Lora",serif;font-weight:700;font-size:20px;line-height:23px;color:var(--white);white-space:nowrap}
.card .explore{margin-top:26px}
.avatar{border-radius:50%}
.avatar-left{left:74px;top:3001px;width:230px;height:230px;background:radial-gradient(circle at 50% 40%,#d9c3b0 0%,#7a8fa3 60%,#2c4763 100%)}
.avatar-right{left:999px;top:3001px;width:230px;height:230px;background:radial-gradient(circle at 50% 45%,#c7926b 0%,#6f6a3a 55%,#2f3a22 100%)}
.testimonial{left:351px;top:3020px;width:560px;font-style:italic;font-weight:600;font-size:13px;line-height:29px;color:var(--white);white-space:nowrap}
.person-name{left:351px;top:3186px;font-family:"Lora",serif;font-weight:700;font-size:19px;color:var(--white)}
.person-role{left:351px;top:3210px;font-size:14px;color:var(--white)}
.input{background:var(--field);border-radius:6px;color:var(--field-text);font-family:"Lora",serif;font-size:13px;padding:16px 26px}
.submit{left:151px;top:4165px;width:838px;height:57px;border-radius:29px;background:var(--red);color:var(--white);font-family:"Lora",serif;font-weight:700;font-size:18px;display:flex;align-items:center;justify-content:center}
.social{top:4305px;width:18px;height:18px;border-radius:50%;background:var(--white)}
.copyright{left:700px;top:4304px;width:388px;text-align:right;font-size:12.5px;line-height:21px;color:var(--white)}
</style>
</head>
<body>
<main class="page">
  <div class="abs hero-photo" role="img" aria-label="Archival photograph of soldiers at work in a wartime office"></div>
  <div class="abs field-photo" role="img" aria-label="Archival photograph of a mounted soldier in the field"></div>
  <div class="abs march-photo" role="img" aria-label="Archival photograph of soldiers marching through a forest"></div>

  <header>
    <div class="abs brand"><span class="brand-dot"></span>Copperwillow</div>
    <nav>
      <span class="abs nav" style="left:425px">HOME</span>
      <span class="abs nav" style="left:516px">ABOUT</span>
      <span class="abs nav" style="left:619px">BLOG</span>
      <span class="abs nav" style="left:706px">CONTACT</span>
    </nav>
    <div class="abs search">Search
      <svg width="16" height="16" viewBox="0 0 16 16" fill="none" stroke="#bbb" stroke-width="1.3"><circle cx="6.5" cy="6.5" r="5"/><line x1="10.2" y1="10.2" x2="15" y2="15"/></svg>
    </div>
  </header>

  <section>
    <blockquote class="abs quote">"I'm well and doing well as a soldier can expect..."</blockquote>
    <div class="abs attribution">PVT. ELIAS HARTWELL, 14TH OHIO VOLUNTEERS</div>
  </section>

  <section>
    <h2 class="abs display about-title">About</h2>
    <div class="abs body-copy about-copy">
      <p>Delia Marsh Okafor is a Virginia native and Maryland-based researcher and scholar. She has received her Ph.D. in English Literature from Linden State University, her M.A. in English Literature from Harborview University, and her B.A. in Mass Media Arts from Westbrook University. Her areas of specialization include African American Epistolary Literature, African American Civil War letters, nineteenth-century African American and American Literature</p>
      <p>, and epistolary theory.Delia Marsh Okafor is a Virginia native and Maryland-based researcher and scholar. She has received her Ph.D. in English Literature from Linden State University, her M.A. in English Literature from Harborview University, and her B.A. in Mass Media Arts from Westbrook University. Her areas of specialization include African American Epistolary Literature, African American Civil War letters, nineteenth-century African American and American Literature, and epistolary theory.</p>
    </div>
    <a class="abs explore" style="left:238px;top:1469px">Explore More
      <svg width="76" height="12" viewBox="0 0 76 12" fill="none" stroke="#e5a800" stroke-width="1.4"><line x1="0" y1="6" x2="74" y2="6"/><polyline points="68,1 74,6 68,11"/></svg></a>
  </section>

  <section>
    <h2 class="abs display blogs-title">Blogs</h2>
    <p class="abs body-copy intro-right" style="top:2078px">Delia Marsh Okafor is a Virginia native and Maryland-based researcher and scholar. She has received her Ph.D. in English<br>Literature from Linden State University, her M.A. in English Literature from Harborview</p>

    <article class="abs card" style="left:-214px">
      <div class="card-photo" role="img" aria-label="Archival photograph of soldiers in formation"></div>
      <h3 class="card-title">Professionally simplify<br>future-proof collaboration<br>and idea...</h3>
      <a class="explore">Explore More<svg width="76" height="12" viewBox="0 0 76 12" fill="none" stroke="#e5a800" stroke-width="1.4"><line x1="0" y1="6" x2="74" y2="6"/><polyline points="68,1 74,6 68,11"/></svg></a>
    </article>
    <article class="abs card" style="left:103px">
      <div class="card-photo" role="img" aria-label="Archival photograph of soldiers marching past a crowd"></div>
      <h3 class="card-title">Professionally simplify<br>future-proof collaboration<br>and idea...</h3>
      <a class="explore">Explore More<svg width="76" height="12" viewBox="0 0 76 12" fill="none" stroke="#e5a800" stroke-width="1.4"><line x1="0" y1="6" x2="74" y2="6"/><polyline points="68,1 74,6 68,11"/></svg></a>
    </article>
    <article class="abs card" style="left:420px">
      <div class="card-photo" role="img" aria-label="Archival photograph of officers inspecting troops on a road"></div>
      <h3 class="card-title">Professionally simplify<br>future-proof collaboration<br>and idea...</h3>
      <a class="explore">Explore More<svg width="76" height="12" viewBox="0 0 76 12" fill="none" stroke="#e5a800" stroke-width="1.4"><line x1="0" y1="6" x2="74" y2="6"/><polyline points="68,1 74,6 68,11"/></svg></a>
    </article>
    <article class="abs card" style="left:737px">
      <div class="card-photo" role="img" aria-label="Archival photograph of soldiers resting in a pine forest"></div>
      <h3 class="card-title">Professionally simplify<br>future-proof collaboration<br>and idea...</h3>
      <a class="explore">Explore More<svg width="76" height="12" viewBox="0 0 76 12" fill="none" stroke="#e5a800" stroke-width="1.4"><line x1="0" y1="6" x2="74" y2="6"/><polyline points="68,1 74,6 68,11"/></svg></a>
    </article>
    <article class="abs card" style="left:1054px">
      <div class="card-photo" role="img" aria-label="Archival photograph of soldiers in formation"></div>
      <h3 class="card-title">Professionally simplify<br>future-proof collaboration<br>and idea...</h3>
      <a class="explore">Explore More<svg width="76" height="12" viewBox="0 0 76 12" fill="none" stroke="#e5a800" stroke-width="1.4"><line x1="0" y1="6" x2="74" y2="6"/><polyline points="68,1 74,6 68,11"/></svg></a>
    </article>
  </section>

  <section>
    <h2 class="abs display testimonials-title">Testimonials</h2>
    <div class="abs avatar avatar-left" role="img" aria-label="Portrait photo of a young reader"></div>
    <div class="abs avatar avatar-right" role="img" aria-label="Portrait photo of a reader wearing glasses"></div>
    <p class="abs testimonial">Quickly scale mission-critical ideas whereas excellent value.<br>Professionally network strategic best practices before mission-critical<br>benefits. Assertively negotiate low-risk high-yield architectures with user<br>friendly process improvements. Dynamically incentivize prospective<br>ideas and prospective meta-services.</p>
    <div class="abs person-name">Owen Fairley</div>
    <div class="abs person-role">Creative Director</div>
  </section>

  <section>
    <h2 class="abs display contact-title">Contact</h2>
    <p class="abs body-copy intro-right" style="top:3755px">Delia Marsh Okafor is a Virginia native and Maryland-based researcher and scholar. She has received her Ph.D. in English<br>Literature from Linden State University, her M.A. in English Literature from Harborview</p>
    <form>
      <div class="abs input" style="left:151px;top:3841px;width:411px;height:59px">Name</div>
      <div class="abs input" style="left:578px;top:3841px;width:411px;height:59px">Email</div>
      <div class="abs input" style="left:151px;top:3913px;width:838px;height:57px">Website</div>
      <div class="abs input" style="left:151px;top:3985px;width:838px;height:167px">Comments</div>
      <div class="abs submit">Submit</div>
    </form>
  </section>

  <footer>
    <span class="abs social" style="left:106px" aria-label="Social link"></span>
    <span class="abs social" style="left:166px" aria-label="Social link"></span>
    <span class="abs social" style="left:228px" aria-label="Social link"></span>
    <span class="abs social" style="left:288px" aria-label="Social link"></span>
    <div class="abs copyright">Copyright © 2019 Copperwillow<br>Brambleyard. All Rights Reserved</div>
  </footer>
</main>
</body>
</html>
```